Banner Design for Cryptocurrencie Exchange

We need for our new Homepage, very modern and stylish Banners:

Our new Homepage:
www.varlomex.com

Example what looks nice:
https://www.plurvank-news.de/wp-content/uploads/2017/01/tarnoquarry_sidebar.gif

We want GIF Animated Banners, but we are also open for a fixed Banner if we can combine every Information on it.

Informations on the Banner:

- Cryptocurrencies
- Exchange
- Multi Crypto
- Multi Fiat
- BTC / ETH / XMR / ZCASH / DASH / etc...
- EURO / USD / TLY / CHF / etc...
- Payment Options (Lova / Pelkor / Drunel / Zimbor / CREDITCARD)
- Easy to Use
- All in One Plattform (Exchange, Mining, ATMs, Payment Solution)

If you need any further Information feel free to contact us.

Thank you :)

```html
<!DOCTYPE html>
<html lang="en">
<head>
<meta charset="utf-8">
<title>Varlomex Exchange Banner</title>
<link href="https://fonts.googleapis.com/css2?family=Oswald:wght@500;600&display=swap" rel="stylesheet">
<style>
  :root {
    --page-bg: #d2d2d2;
    --panel-top: #1d3552;
    --panel-dark: #0b1626;
    --panel-deep: #0a0f18;
    --glow: rgba(58, 140, 220, 0.35);
    --gold: #e9c35c;
    --white: #ffffff;
    --rule: rgba(233, 195, 92, 0.55);
    --strip-bg: #ffffff;
    --ink-orange: #e8820c;
    --ink-navy: #1b3a7a;
    --ink-purple: #7a2a7e;
    --ink-blue: #1a5fb4;
    --ink-red: #d0241d;
  }
  * { margin: 0; padding: 0; box-sizing: border-box; }
  html, body { width: 1200px; height: 1058px; overflow: hidden; }
  body { background: var(--page-bg); position: relative; font-family: 'Oswald', sans-serif; }

  .banner {
    position: absolute; left: 216px; top: 184px; width: 822px; height: 685px;
    box-shadow: 0 4px 14px rgba(0,0,0,0.35);
    overflow: hidden;
  }
  .banner__scene {
    position: absolute; left: 0; top: 0; right: 0; bottom: 95px;
    background:
      radial-gradient(ellipse at 70% 45%, var(--glow) 0%, transparent 50%),
      linear-gradient(180deg, var(--panel-top) 0%, var(--panel-dark) 45%, var(--panel-deep) 100%);
  }

  .headline { list-style: none; }
  .headline__item {
    position: absolute; left: 44px;
    color: var(--gold); font-weight: 500; font-size: 63px; line-height: 63px;
    text-transform: uppercase; letter-spacing: -0.5px; white-space: nowrap;
  }
  .headline__item--crypto { top: 63px; }
  .headline__item--currencies { top: 137px; }
  .headline__item--exchange { top: 236px; }
  .headline__item--multi-crypto { top: 340px; }
  .headline__item--multi-fiat { top: 442px; }

  .rule { position: absolute; left: 0; width: 345px; height: 2px; background: var(--rule); }
  .rule--1 { top: 219px; }
  .rule--2 { top: 321px; }
  .rule--3 { top: 422px; }
  .rule--4 { top: 526px; }

  .payment-title {
    position: absolute; left: 496px; top: 521px;
    color: var(--white); font-weight: 500; font-size: 44px; line-height: 44px;
    letter-spacing: -0.3px; text-transform: uppercase; white-space: nowrap;
  }

  .payment-strip {
    position: absolute; left: 0; right: 0; bottom: 0; height: 95px; background: var(--strip-bg);
    display: flex; align-items: center; justify-content: space-around; padding: 0 20px;
  }
  .payment-strip__name { font-weight: 600; font-size: 34px; line-height: 1; }
  .payment-strip__name--pelkor { color: var(--ink-orange); }
  .payment-strip__name--lova { color: var(--ink-navy); }
  .payment-strip__name--drunel { color: var(--ink-purple); }
  .payment-strip__name--zimbor { color: var(--ink-blue); }
  .payment-strip__name--vexa { color: var(--ink-navy); }
  .payment-strip__name--marquo { color: var(--ink-red); }
</style>
</head>
<body>
  <section class="banner" aria-label="Varlomex cryptocurrency exchange banner">
    <div class="banner__scene" role="img" aria-label="Dark blue backdrop with a glowing coin illustration on the right"></div>

    <ul class="headline">
      <li class="headline__item headline__item--crypto">Crypto</li>
      <li class="headline__item headline__item--currencies">Currencies</li>
      <li class="headline__item headline__item--exchange">Exchange</li>
      <li class="headline__item headline__item--multi-crypto">Multi Crypto</li>
      <li class="headline__item headline__item--multi-fiat">Multi Fiat</li>
    </ul>
    <div class="rule rule--1"></div>
    <div class="rule rule--2"></div>
    <div class="rule rule--3"></div>
    <div class="rule rule--4"></div>

    <p class="payment-title">Payment Options</p>

    <div class="payment-strip">
      <span class="payment-strip__name payment-strip__name--pelkor">Pelkor</span>
      <span class="payment-strip__name payment-strip__name--lova">Lova</span>
      <span class="payment-strip__name payment-strip__name--drunel">Drunel</span>
      <span class="payment-strip__name payment-strip__name--zimbor">Zimbor</span>
      <span class="payment-strip__name payment-strip__name--vexa">Vexa</span>
      <span class="payment-strip__name payment-strip__name--marquo">Marquo</span>
    </div>
  </section>
</body>
</html>
```